New bussiness card, using company logo.
Gerald Finch
Manager/Director
Finch Property Developments
Po Box 4637
Thuringowa Central
Qld
0412 558 306
gerald@finchpropertydevelopments
eye catching, vibrant colours, professional

It Company

```html
<!DOCTYPE html>
<html lang="en">
<head>
<meta charset="utf-8">
<title>Finch Property Developments – Business Card</title>
<link href="https://fonts.googleapis.com/css2?family=Open+Sans:wght@400;700&family=Yellowtail&display=swap" rel="stylesheet">
<style>
  :root {
    --backdrop: #3a3a3a;
    --brand-green: #72b944;
    --brand-red: #e0261f;
    --card-white: #f3f3f3;
    --label-white: #f4f4f4;
    --ink-soft: #4a4a4a;
  }
  * { box-sizing: border-box; margin: 0; padding: 0; }
  html, body {
    width: 1200px;
    height: 933px;
    overflow: hidden;
    background: var(--backdrop);
    font-family: "Open Sans", Arial, sans-serif;
  }
  .canvas { position: relative; width: 1200px; height: 933px; }

  .card { position: absolute; width: 525px; height: 300px; }

  /* Front */
  .card-front { left: 340px; top: 149px; background: var(--brand-green); }
  .front-brand {
    position: absolute;
    left: 0; right: 0; top: 78px;
    display: flex;
    justify-content: center;
    align-items: center;
    gap: 16px;
  }
  .brand-mark { width: 24px; height: 24px; background: #ffffff; flex: none; }
  .front-brand-name {
    color: #ffffff;
    font-weight: 700;
    font-size: 33px;
    letter-spacing: 0.5px;
    text-transform: uppercase;
    line-height: 1.12;
  }
  .name-label {
    position: absolute;
    left: 48px; top: 214px;
    width: 429px; height: 69px;
    background: var(--label-white);
  }

  /* Back */
  .card-back { left: 341px; top: 489px; background: var(--card-white); }
  .contact-block {
    position: absolute; left: 50px; top: 42px;
    color: var(--ink-soft); font-size: 11.5px; line-height: 17px;
  }
  .person-name {
    font-family: "Yellowtail", "Brush Script MT", cursive;
    font-weight: 400;
    color: var(--brand-red);
    font-size: 29px;
    line-height: 34px;
  }
  .address { margin-top: 23px; }
  .contact-lines { margin-top: 24px; }
  .contact-label {
    font-family: "Yellowtail", "Brush Script MT", cursive;
    color: var(--brand-red);
    font-size: 14px;
    margin-right: 4px;
  }
  .web { color: var(--brand-red); }
  .back-brand {
    position: absolute;
    left: 281px; top: 124px;
    width: 200px;
    display: flex;
    align-items: center;
    gap: 9px;
  }
  .back-brand .brand-mark { width: 16px; height: 16px; background: var(--brand-red); }
  .back-brand-name {
    color: var(--brand-red);
    font-weight: 700;
    font-size: 17px;
    line-height: 1.15;
    text-transform: uppercase;
  }
</style>
</head>
<body>
<main class="canvas">
  <section class="card card-front" aria-label="Card front">
    <div class="front-brand">
      <span class="brand-mark"></span>
      <span class="front-brand-name">Finch Property<br>Developments</span>
    </div>
    <div class="name-label"></div>
  </section>

  <section class="card card-back" aria-label="Card back">
    <div class="contact-block">
      <h1 class="person-name">Gerald Finch</h1>
      <p>Manager/Director</p>
      <p>Real Estage agent LIC no. 4827305</p>
      <div class="address">
        <p>Finch Property Developments</p>
        <p>Po Box 4637</p>
        <p>Marlow Central, Qld</p>
      </div>
      <div class="contact-lines">
        <p><span class="contact-label">phone:</span>0412 558 306</p>
        <p><span class="contact-label">email:</span>gerald@finchpropertydevelopments.com</p>
        <p class="web">www.finchpropertydevelopments.com.au</p>
      </div>
    </div>
    <div class="back-brand">
      <span class="brand-mark"></span>
      <span class="back-brand-name">Finch Property<br>Developments</span>
    </div>
  </section>
</main>
</body>
</html>
```